INTERNATIONAL COMPANY IN MARITIME AIR TRANSPORT AND LOGISTICS

We need a power point model with the attached logo, we organize the transport of goods around the world by plane and boat. We also organize logistics. We would like a creation in the colors of our logo or in agreement with this one. The final design must convey the openness to international, men at the heart of our service and the strength of our company.

Target Market(s)

LUX - Aeronautics - RETAIL

Industry/Entity Type

Retail

Font styles to use
Serif

Colors

Requirements
Must have
• We need a power point model with the attached logo, we organize the transport of goods around the world by plane and boat. We also organize logistics. We would like a creation in the colors of our logo or in agreement with this one. The final design must convey the openness to international, men at the heart of our service and the strength of our company.
Nice to have
Should not have
• FREE

```html
<!DOCTYPE html>
<html lang="en">
<head>
<meta charset="utf-8">
<title>Marivane – Presentation Template</title>
<link rel="stylesheet" href="https://fonts.googleapis.com/css2?family=Montserrat:wght@400;500;600;700&display=swap">
<style>
  :root{
    --stage:#000;
    --paper:#fff;
    --blue:#13a4e3;
    --blue-light:#4fc3f0;
    --ink:#1f2d3d;
    --body:#4a5561;
    --grey:#cfd5dd;
    --footer:#e6eaee;
    --photo-a:#8a8f93;
    --photo-b:#c7c4bb;
  }
  *{box-sizing:border-box;margin:0;padding:0}
  html,body{width:1200px;height:697px;overflow:hidden;background:var(--stage)}
  body{position:relative;font-family:"Montserrat",sans-serif;color:var(--ink)}

  .slide{position:absolute;width:390px;height:220px;background:var(--paper);overflow:hidden}
  .col-1{left:6px}.col-2{left:406px}.col-3{left:805px}
  .row-1{top:8px}.row-2{top:236px}.row-3{top:472px}

  .slide-title{position:absolute;left:0;top:10px;padding-left:8px;border-left:3px solid var(--blue);
    font-size:14px;font-weight:600;line-height:16px;color:var(--ink)}
  .slide-title b{color:var(--blue);font-weight:700}

  .brand{position:absolute;right:10px;top:8px;display:flex;align-items:center;gap:4px;
    font-size:7.5px;font-weight:500;letter-spacing:1px;color:var(--ink)}
  .brand i{width:7px;height:7px;background:var(--blue);display:block}

  .footer{position:absolute;left:0;right:0;bottom:0;height:10px;background:var(--footer);
    font-size:5px;line-height:10px;padding-left:6px;color:#6b7680;letter-spacing:.5px}
  .footer .page{position:absolute;right:0;top:0;width:42px;height:10px;background:var(--blue);
    color:#fff;text-align:center;font-weight:600}

  .para-title{font-size:8.5px;font-weight:600;color:var(--blue);margin-bottom:3px;position:relative}
  .para-title.dot{padding-left:10px}
  .para-title.dot::before{content:"";position:absolute;left:0;top:2.5px;width:5px;height:5px;border-radius:50%;
    background:var(--ink);box-shadow:0 0 0 1px #fff,0 0 0 2px var(--grey)}
  .para-title.small{font-size:7px;color:var(--ink);margin-bottom:1px}
  .copy{font-size:5.2px;line-height:9px;color:var(--body);text-align:justify}
  .copy.left{text-align:left}

  .bullet{position:relative;padding-left:13px;text-align:left;line-height:7.5px}
  .bullet::before{content:"";position:absolute;left:0;top:2px;width:5px;height:5px;border-radius:50%;background:var(--ink)}

  .office-list{list-style:none;font-size:7px;color:var(--body);line-height:14.5px}
  .office-list li{position:relative;padding-left:9px}
  .office-list li::before{content:"";position:absolute;left:0;top:5px;width:4px;height:4px;border-radius:50%;background:var(--blue)}

  .placeholder{position:absolute;background:var(--grey)}
  .photo{position:absolute;background:linear-gradient(160deg,var(--photo-a),var(--photo-b) 60%,#6f7478)}
  .block{position:absolute}
</style>
</head>
<body>

<!-- Slide 1: two image columns -->
<section class="slide col-1 row-1">
  <h2 class="slide-title"><b>Project</b> Title here</h2>
  <div class="brand"><i></i>MARIVANE</div>
  <div class="placeholder" style="left:22px;top:40px;width:160px;height:73px" role="img" aria-label="Image placeholder"></div>
  <div class="placeholder" style="left:218px;top:40px;width:160px;height:73px" role="img" aria-label="Image placeholder"></div>
  <div class="block" style="left:12px;top:122px;width:182px">
    <h3 class="para-title dot">Paragraph Title here</h3>
    <p class="copy">sed diam nonummy nibh euismod tincidunt ut laoreet dolore magna aliquam erat volutpat. Ut wisi enim ad minim veniam, quis nostrud exerci tation ullamcorper suscipit lobortis nisl ut aliquip ex ea commodo consequat. Duis autem vel eum iriure dolor in hendrerit in vulputate velit esse molestie consequat sed diam nonummy nibh euismod tincidunt ut laoreet dolore magna aliquam erat volutpat. Ut wisi enim ad minim veniam, quis nostrud</p>
  </div>
  <div class="block" style="left:204px;top:122px;width:178px">
    <h3 class="para-title dot">Paragraph Title here</h3>
    <p class="copy">sed diam nonummy nibh euismod tincidunt ut laoreet dolore magna aliquam erat volutpat. Ut wisi enim ad minim veniam, quis nostrud exerci tation ullamcorper suscipit lobortis nisl ut aliquip ex ea commodo consequat. Duis autem vel eum iriure dolor in hendrerit in vulputate velit esse molestie consequat sed diam nonummy nibh euismod tincidunt ut laoreet dolore magna aliquam erat volutpat. Ut wisi enim ad minim veniam, quis nostrud</p>
  </div>
  <div class="footer">www.marivane.net<span class="page">Page : 01</span></div>
</section>

<!-- Slide 2: text with photo -->
<section class="slide col-2 row-1">
  <h2 class="slide-title"><b>Project</b> Title here</h2>
  <div class="brand"><i></i>MARIVANE</div>
  <div class="block" style="left:8px;top:62px;width:182px">
    <h3 class="para-title dot">Paragraph Title here</h3>
    <p class="copy">sed diam nonummy nibh euismod tincidunt ut laoreet dolore magna aliquam erat volutpat. Ut wisi enim ad minim veniam, quis nostrud exerci tation ullamcorper suscipit lobortis nisl ut aliquip ex ea commodo consequat. Duis autem vel eum iriure dolor in hendrerit in vulputate velit esse molestie consequat sed diam nonummy nibh euismod tincidunt ut laoreet dolore magna aliquam erat volutpat. Ut wisi enim ad minim veniam, quis nostrud exerci tation ullamcorper suscipit lobortis nisl ut aliquip ex ea commodo consequat. Duis autem vel eum iriure dolor in hendrerit in vulputate velit esse molestie consequat sed diam nonummy nibh euismod tincidunt ut laoreet dolore magna aliquam erat volutpat. Ut wisi enim ad minim veniam</p>
  </div>
  <div class="photo" style="left:196px;top:55px;width:184px;height:137px" role="img" aria-label="Photo of a warehouse loading dock with forklifts and cargo trailers"></div>
  <div class="footer">www.marivane.net<span class="page">Page : 01</span></div>
</section>

<!-- Slide 3: two text columns -->
<section class="slide col-3 row-1">
  <h2 class="slide-title"><b>Project</b> Title here</h2>
  <div class="brand"><i></i>MARIVANE</div>
  <div class="block" style="left:8px;top:62px;width:182px">
    <h3 class="para-title dot">Paragraph Title here</h3>
    <p class="copy">sed diam nonummy nibh euismod tincidunt ut laoreet dolore magna aliquam erat volutpat. Ut wisi enim ad minim veniam, quis nostrud exerci tation ullamcorper suscipit lobortis nisl ut aliquip ex ea commodo consequat. Duis autem vel eum iriure dolor in hendrerit in vulputate velit esse molestie consequat sed diam nonummy nibh euismod tincidunt ut laoreet dolore magna aliquam erat volutpat. Ut wisi enim ad minim veniam, quis nostrud exerci tation ullamcorper suscipit lobortis nisl ut aliquip ex ea commodo consequat. Duis autem vel eum iriure dolor in hendrerit in vulputate velit esse molestie consequat sed diam nonummy nibh euismod tincidunt ut laoreet dolore magna aliquam erat volutpat. Ut wisi enim ad minim veniam</p>
  </div>
  <div class="block" style="left:200px;top:62px;width:182px">
    <h3 class="para-title dot">Paragraph Title here</h3>
    <p class="copy">sed diam nonummy nibh euismod tincidunt ut laoreet dolore magna aliquam erat volutpat. Ut wisi enim ad minim veniam, quis nostrud exerci tation ullamcorper suscipit lobortis nisl ut aliquip ex ea commodo consequat. Duis autem vel eum iriure dolor in hendrerit in vulputate velit esse molestie consequat sed diam nonummy nibh euismod tincidunt ut laoreet dolore magna aliquam erat volutpat. Ut wisi enim ad minim veniam, quis nostrud exerci tation ullamcorper suscipit lobortis nisl ut aliquip ex ea commodo consequat. Duis autem vel eum iriure dolor in hendrerit in vulputate velit esse molestie consequat sed diam nonummy nibh euismod tincidunt ut laoreet dolore magna aliquam erat volutpat. Ut wisi enim ad minim veniam</p>
  </div>
  <div class="footer">www.marivane.net<span class="page">Page : 01</span></div>
</section>

<!-- Slide 4: cover -->
<section class="slide col-1 row-2" style="background:linear-gradient(115deg,#f2f8fc,#fff 55%)">
  <div class="block" style="right:22px;top:92px;text-align:right">
    <div style="display:flex;align-items:center;justify-content:flex-end;gap:8px">
      <i style="display:block;width:18px;height:18px;background:var(--blue)"></i>
      <span style="font-size:28px;font-weight:500;letter-spacing:3px;color:var(--ink);line-height:30px">MARIVANE</span>
    </div>
    <p style="font-size:7.5px;font-weight:500;letter-spacing:1px;color:var(--ink);margin-top:6px">WE MOVE WHAT MATTERS</p>
    <p style="font-size:14px;font-weight:500;letter-spacing:1.8px;color:var(--blue);margin-top:22px">PROJECT TITLE HERE</p>
    <p style="font-size:9.5px;color:var(--blue);margin-top:1px">Subtext here</p>
  </div>
</section>

<!-- Slide 5: photo with blue panel -->
<section class="slide col-2 row-2">
  <h2 class="slide-title"><b>Project</b> Title here</h2>
  <div class="brand"><i></i>MARIVANE</div>
  <div class="photo" style="left:0;top:54px;width:161px;height:152px" role="img" aria-label="Photo of a yellow forklift beside stacked pallets at a loading dock"></div>
  <div class="block" style="left:163px;top:54px;width:227px;height:152px;background:var(--blue);padding:8px 7px;color:#fff">
    <h3 style="font-size:8.5px;font-weight:600;margin-bottom:5px">Paragraph Title here</h3>
    <p class="copy" style="color:#fff;font-size:5px">sed diam nonummy nibh euismod tincidunt ut laoreet dolore magna aliquam erat volutpat. Ut wisi enim ad minim veniam, quis nostrud exerci tation ullamcorper suscipit lobortis nisl ut aliquip ex ea commodo consequat. Duis autem vel eum iriure dolor in hendrerit in vulputate velit esse molestie consequat, vel illum dolore eu feugiat nulla facilisis at vero eros et accumsan et iusto odio dignissim qui blandit praesent luptatum zzril delenit augue duis dolore te feugait nulla facilisi.</p>
    <p class="copy" style="color:#fff;font-size:5px;margin-top:8px">Lorem ipsum dolor sit amet, cons ectetuer adipiscing elit, sed diam nonummy nibh euismod tincidunt ut laoreet dolore magna aliquam erat volutpat. Ut wisi enim ad minim veniam.</p>
  </div>
  <div class="footer">www.marivane.net<span class="page">Page : 01</span></div>
</section>

<!-- Slide 6: stacked paragraphs -->
<section class="slide col-3 row-2">
  <h2 class="slide-title"><b>Project</b> Title here</h2>
  <div class="brand"><i></i>MARIVANE</div>
  <div class="block" style="left:26px;top:45px;width:354px">
    <h3 class="para-title small">Paragraph Title here</h3>
    <p class="copy left">sed diam nonummy nibh euismod tincidunt ut laoreet dolore magna aliquam erat volutpat. Ut wisi enim ad minim veniam, quis nostrud exerci tation ullamcorper suscipit lobortis nisl ut aliquip ex ea commodo consequat. Duis autem vel eum iriure dolor in hendrerit in vulputate velit esse molestie consequat</p>
    <h3 class="para-title small" style="margin-top:10px">Paragraph Title here</h3>
    <p class="copy left">sed diam nonummy nibh euismod tincidunt ut laoreet dolore magna aliquam erat volutpat. Ut wisi enim ad minim veniam, quis nostrud exerci tation ullamcorper suscipit lobortis nisl ut aliquip ex ea commodo consequat. Duis autem vel eum iriure dolor in hendrerit in vulputate velit esse molestie consequat</p>
    <h3 class="para-title small" style="margin-top:10px">Paragraph Title here</h3>
    <p class="copy left">sed diam nonummy nibh euismod tincidunt ut laoreet dolore magna aliquam erat volutpat. Ut wisi enim ad minim veniam, quis nostrud exerci tation ullamcorper suscipit lobortis nisl ut aliquip ex ea commodo consequat. Duis autem vel eum iriure dolor in hendrerit in vulputate velit esse molestie consequat sed diam nonummy nibh euismod tincidunt ut laoreet dolore magna aliquam erat volutpat. Ut wisi enim ad minim veniam, quis nostrud exerci tation ullamcorper suscipit lobortis nisl ut aliquip ex ea commodo consequat. Duis autem vel eum iriure dolor in hendrerit in vulputate velit esse molestie consequat</p>
  </div>
  <div class="footer">www.marivane.net<span class="page">Page : 01</span></div>
</section>

<!-- Slide 7: bullet list with photo -->
<section class="slide col-1 row-3">
  <h2 class="slide-title"><b>Project</b> Title here</h2>
  <div class="brand"><i></i>MARIVANE</div>
  <div class="block" style="left:15px;top:52px;width:195px">
    <h3 class="para-title" style="margin-bottom:8px">Paragraph Title here</h3>
    <p class="copy bullet">sed diam nonummy nibh euismod tincidunt ut laoreet dolore magna aliquam erat volutpat. Ut wisi enim ad minim veniam, quis nostrud exerci tation ullamcorper suscipit lobortis nisl ut aliquip ex ea commodo consequat</p>
    <p class="copy bullet" style="margin-top:6px">sed diam nonummy nibh euismod tincidunt ut laoreet dolore magna aliquam erat volutpat. Ut wisi enim ad minim veniam, quis nostrud exerci tation ullamcorper suscipit lobortis nisl ut aliquip ex ea commodo consequat</p>
    <p class="copy bullet" style="margin-top:14px">sed diam nonummy nibh euismod tincidunt ut laoreet dolore magna aliquam erat volutpat. Ut wisi enim ad minim veniam, quis nostrud exerci tation ullamcorper suscipit lobortis nisl ut aliquip ex ea commodo consequat</p>
  </div>
  <div class="photo" style="left:218px;top:36px;width:166px;height:165px;background:linear-gradient(170deg,#5d6a78,#b9a58c 55%,#d9d4ca)" role="img" aria-label="Photo of tall warehouse racking with a bonded zone sign"></div>
  <div class="footer">www.marivane.net<span class="page">Page : 01</span></div>
</section>

<!-- Slide 8: progress charts -->
<section class="slide col-2 row-3">
  <h2 class="slide-title"><b>Project</b> Title here</h2>
  <div class="brand"><i></i>MARIVANE</div>
  <div class="block" style="left:28px;top:40px;width:350px">
    <h3 class="para-title small" style="color:var(--ink)">Paragraph Title here</h3>
    <p class="copy left">sed diam nonummy nibh euismod tincidunt ut laoreet dolore magna aliquam erat volutpat. Ut wisi enim ad minim veniam, quis nostrud exerci tation ullamcorper suscipit lobortis nisl ut aliquip ex ea commodo consequat. sed diam nonummy nibh euismod tincidunt ut laoreet dolore magna aliquam erat volutpat. Ut wisi enim ad minim veniam.</p>
  </div>
  <svg class="block" style="left:0;top:96px" width="390" height="110" viewBox="0 0 390 110" font-family="Montserrat, sans-serif">
    <g fill="none" stroke-width="3.5">
      <circle cx="57" cy="37" r="27" stroke="#eef1f4"/>
      <circle cx="57" cy="37" r="27" stroke="#13a4e3" stroke-dasharray="135.7 169.6" transform="rotate(-90 57 37)"/>
      <circle cx="156" cy="37" r="27" stroke="#eef1f4"/>
      <circle cx="156" cy="37" r="27" stroke="#bfc4c9" stroke-dasharray="84.8 169.6" transform="rotate(-90 156 37)"/>
      <circle cx="243" cy="37" r="27" stroke="#eef1f4"/>
      <circle cx="243" cy="37" r="27" stroke="#4fc3f0" stroke-dasharray="118.7 169.6" transform="rotate(-90 243 37)"/>
      <circle cx="336" cy="37" r="27" stroke="#eef1f4"/>
      <circle cx="336" cy="37" r="27" stroke="#d3d9df" stroke-dasharray="101.8 169.6" transform="rotate(-90 336 37)"/>
    </g>
    <g font-size="9" text-anchor="middle" fill="#3a4450">
      <text x="57" y="40" fill="#13a4e3">80%</text>
      <text x="156" y="40">50%</text>
      <text x="243" y="40" fill="#13a4e3">70%</text>
      <text x="336" y="40">60%</text>
    </g>
    <g font-size="6.8" font-weight="600" text-anchor="middle">
      <text x="57" y="81" fill="#1f2d3d">Graphics Chart</text>
      <text x="156" y="81" fill="#c5cad0">Graphics Chart</text>
      <text x="243" y="81" fill="#1f2d3d">Graphics Chart</text>
      <text x="336" y="81" fill="#c5cad0">Graphics Chart</text>
    </g>
    <g font-size="5" text-anchor="middle" fill="#4a5561">
      <text x="57" y="93">sed diam nonummy nibh</text><text x="57" y="100">euismod tincidunt ut laoreet</text>
      <text x="156" y="93">sed diam nonummy nibh</text><text x="156" y="100">euismod tincidunt ut laoreet</text>
      <text x="243" y="93">sed diam nonummy nibh</text><text x="243" y="100">euismod tincidunt ut laoreet</text>
      <text x="336" y="93">sed diam nonummy nibh</text><text x="336" y="100">euismod tincidunt ut laoreet</text>
    </g>
  </svg>
  <div class="footer">www.marivane.net<span class="page">Page : 01</span></div>
</section>

<!-- Slide 9: offices -->
<section class="slide col-3 row-3">
  <h2 class="slide-title"><b>Our organization in</b> China</h2>
  <div class="brand"><i></i>MARIVANE</div>
  <ul class="block office-list" style="left:16px;top:44px">
    <li>Hong Kong</li><li>Shanghai</li><li>Qingdao</li><li>Dalian</li><li>Fuzhou</li><li>Ningbo</li>
    <li>Tianjin</li><li>Xiamen</li><li>Shenzen</li><li>Guangzhou</li><li>Beijing</li>
  </ul>
  <div class="block" style="left:136px;top:24px;width:254px;height:186px;background:radial-gradient(ellipse at 60% 55%,#d6ecf8,#fff 72%)" role="img" aria-label="Dotted map of China marking office locations"></div>
  <div class="footer">www.marivane.net<span class="page">Page : 01</span></div>
</section>

</body>
</html>
```